Medical VIP club - small design

Please read the specs in a design brief attached. Also we don't have logo in a Vector format and attaching the only version we have.

Industry/Entity Type

Club

```html
<!DOCTYPE html>
<html lang="en">
<head>
<meta charset="utf-8">
<title>Medvorin – Medical VIP Club</title>
<link rel="stylesheet" href="https://fonts.googleapis.com/css2?family=Cinzel:wght@400;600&family=Cinzel+Decorative:wght@700&family=Questrial&family=Sorts+Mill+Goudy&family=PT+Sans:wght@400;700&display=swap">
<style>
  :root{
    --outer:#d3bd93;
    --page:#f3ebda;
    --nav:#dccdaa;
    --nav-text:#6e5a43;
    --hero:#e04a22;
    --hero-dark:#b8301a;
    --accent:#d8361a;
    --heading:#7c6a55;
    --body:#6b6156;
    --sidebar:#e9dfc7;
    --line:#d7c8a8;
    --white:#ffffff;
  }
  *{margin:0;padding:0;box-sizing:border-box}
  html,body{width:1200px;height:1052px;overflow:hidden}
  body{background:var(--outer);font-family:"PT Sans",sans-serif;color:var(--body)}
  .page{position:absolute;left:138px;top:0;width:923px;height:1052px;background:var(--page);box-shadow:0 0 8px rgba(90,60,20,.35)}
  .abs{position:absolute}

  /* header */
  .brand{left:28px;top:44px;display:flex;align-items:center;gap:8px}
  .brand-dot{width:26px;height:26px;border-radius:50%;background:#e05a22}
  .brand-name{font-family:"PT Sans",sans-serif;font-weight:700;font-size:40px;color:#d8511e;letter-spacing:.5px;line-height:1}
  .call{left:648px;top:62px;display:flex;gap:8px}
  .call-label{font-family:"Sorts Mill Goudy",serif;color:#8a7b69;font-size:17px;line-height:1.1}
  .call-number{font-family:"Sorts Mill Goudy",serif;color:#8a7b69;font-size:23px;line-height:1.1}

  /* navigation */
  .main-nav{left:0;top:122px;width:923px;height:28px;background:var(--nav);display:flex}
  .main-nav a{font-family:"Cinzel",serif;font-weight:600;font-size:12.5px;color:var(--nav-text);text-decoration:none;display:flex;align-items:center;justify-content:center;height:100%;border-right:1px solid #c9b88f}
  .main-nav a:last-child{border-right:none}

  /* hero */
  .hero{left:0;top:150px;width:923px;height:402px;background:radial-gradient(ellipse at 40% 40%,#ea5a2c 0%,var(--hero) 45%,var(--hero-dark) 100%);overflow:hidden}
  .hero-title{left:69px;top:86px;font-family:"Cinzel Decorative",serif;font-weight:700;font-style:italic;font-size:30px;color:#fff5ea;text-shadow:1px 2px 3px rgba(80,20,0,.5);letter-spacing:.5px}
  .hero-lines{left:70px;top:136px;font-family:"Questrial",sans-serif;font-size:18px;line-height:20.5px;color:#fff5ea}
  .hero-cta{left:64px;top:283px;width:254px;height:38px;border-radius:19px;background:linear-gradient(#fbf6ee,#e2d6c4);box-shadow:0 2px 4px rgba(80,20,0,.4);display:flex;align-items:center;padding-left:16px;font-family:"Questrial",sans-serif;font-size:18px;color:#8a3a1e}
  .hero-cta svg{position:absolute;right:16px;top:10px}
  .hero-portrait{left:505px;top:0;width:418px;height:402px;background:linear-gradient(160deg,#e9b48e 0%,#c9805d 35%,#5a5856 70%,#3d3d3d 100%);border-top-left-radius:140px 200px}
  .hero-notch{left:828px;top:543px}

  /* photo strip */
  .strip{left:4px;top:555px;width:915px;height:84px;display:flex;gap:2px}
  .strip div{height:100%}

  /* welcome */
  .section-title{font-family:"Cinzel",serif;font-size:20px;color:var(--heading)}
  .welcome-title{left:26px;top:654px}
  .welcome-text{left:28px;top:684px;width:600px;font-size:11.3px;line-height:18.5px;color:#6f665b}
  .more{color:var(--accent);font-weight:700;margin-left:12px}

  /* services */
  .services-title{left:27px;top:830px}
  .service{top:866px;width:146px}
  .service-photo{height:74px;border:1px solid #cdbfa5;padding:3px;background:var(--white)}
  .service-photo div{width:100%;height:100%}
  .service-caption{margin-top:10px;font-size:11.5px;color:var(--accent);text-align:center}

  /* sidebar */
  .sidebar{left:668px;top:639px;width:255px;height:225px;background:var(--sidebar);border-left:2px solid #d9cbae}
  .news-title{left:18px;top:14px;font-family:"Sorts Mill Goudy",serif;font-size:21px;color:var(--heading);display:flex;align-items:center;gap:10px}
  .news-item{left:10px;width:240px}
  .news-date{font-size:12.5px;font-weight:700;color:var(--accent);letter-spacing:.3px}
  .news-text{font-size:11.3px;line-height:16.5px;color:#6f665b;margin-top:2px}
  .news-rule{left:8px;top:125px;width:232px;border-top:1px dotted #b5a486}
  .news-more{right:8px;top:203px;font-size:10.5px;font-weight:700;color:#8a7b69}

  .newsletter{left:669px;top:863px;width:254px;height:106px;background:linear-gradient(100deg,#bf3518,#e04a22 60%,#c63a1c)}
  .newsletter-title{left:20px;top:8px;font-family:"Sorts Mill Goudy",serif;font-size:21px;color:var(--white);display:flex;align-items:center;gap:10px}
  .newsletter-input{left:18px;top:43px;width:217px;height:23px;background:#f8f3ea;font-size:10px;color:#7a6d5f;padding:6px 10px}
  .newsletter-btn{left:131px;top:76px;width:106px;height:24px;border-radius:12px;background:linear-gradient(#fdf9f2,#e2d6c4);font-size:11.5px;font-weight:700;color:var(--accent);display:flex;align-items:center;padding-left:22px;box-shadow:0 1px 3px rgba(60,10,0,.4)}
  .newsletter-btn svg{position:absolute;right:10px;top:7px}

  /* footer */
  .footer-rule{left:0;top:980px;width:923px;border-top:1px solid var(--line)}
  .footer-nav{left:0;top:992px;width:923px;display:flex;justify-content:center;font-size:11.8px;color:#5e554b}
  .footer-nav span.sep{margin:0 21px}
  .copyright{left:0;top:1023px;width:923px;text-align:center;font-size:11.3px;color:#5e554b}
</style>
</head>
<body>
<div class="page">

  <header>
    <div class="abs brand">
      <span class="brand-dot"></span>
      <span class="brand-name">medvorin</span>
    </div>
    <div class="abs call">
      <svg width="68" height="46" viewBox="0 0 68 46" aria-hidden="true">
        <ellipse cx="34" cy="42" rx="30" ry="3" fill="#c9b99a"/>
        <path d="M6 14 C10 4 58 4 62 14 L56 20 L48 16 L20 16 L12 20 Z" fill="#2b2b2b"/>
        <path d="M18 18 L50 18 L58 40 L10 40 Z" fill="#333"/>
        <circle cx="34" cy="29" r="8" fill="#555"/>
        <circle cx="34" cy="29" r="3" fill="#bbb"/>
      </svg>
      <div>
        <div class="call-label">Call Us</div>
        <div class="call-number">1800-555-0142</div>
      </div>
    </div>
  </header>

  <nav class="abs main-nav">
    <a style="width:92px;margin-left:8px">HOME</a>
    <a style="width:95px">ABOUT US</a>
    <a style="width:90px">VIP CLUB</a>
    <a style="width:90px">SERVICES</a>
    <a style="width:176px">PACKAGES AND PRICES</a>
    <a style="width:130px">REGISTRATION</a>
    <a style="width:127px">TESTIMONIALS</a>
    <a style="width:104px">CONTACTS</a>
  </nav>

  <section class="abs hero">
    <div class="abs hero-portrait" role="img" aria-label="Smiling businesswoman in a grey blazer"></div>
    <h1 class="abs hero-title">SOME TEXT COMES HERE</h1>
    <p class="abs hero-lines">Some Text comes here<br>Some Text comes here<br>Some Text comes here</p>
    <div class="abs hero-cta">Click here to Register
      <svg width="30" height="18" viewBox="0 0 30 18" aria-hidden="true"><path d="M2 1 L10 9 L2 17 M14 1 L22 9 L14 17" stroke="#d8361a" stroke-width="4" fill="none"/></svg>
    </div>
  </section>
  <svg class="abs hero-notch" width="22" height="10" viewBox="0 0 22 10" aria-hidden="true"><path d="M0 10 L11 0 L22 10 Z" fill="#f3ebda"/></svg>

  <div class="abs strip">
    <div style="width:181px;background:linear-gradient(90deg,#7a1010,#b51e1e,#5a0c0c)" role="img" aria-label="Emergency department sign"></div>
    <div style="width:185px;background:linear-gradient(#c08a3a,#e8c07a 45%,#7b6a58)" role="img" aria-label="Airliner flying above clouds at sunset"></div>
    <div style="width:182px;background:linear-gradient(90deg,#6a4a2a,#b89a6e,#4a3220)" role="img" aria-label="Hotel reception desk with guests"></div>
    <div style="width:182px;background:linear-gradient(#ffffff,#e6ebef)" role="img" aria-label="Team of doctors and nurses"></div>
    <div style="width:179px;background:linear-gradient(90deg,#ffffff,#e8c7ac 55%,#f5efe8)" role="img" aria-label="Smiling businesswoman"></div>
  </div>

  <main>
    <h2 class="abs section-title welcome-title">WELCOME TO OUR SITE</h2>
    <p class="abs welcome-text">Lorem ipsum dolor sit amet, consectetuer adipiscing elit. Aenean commodo ligula eget dolor. Aenean massa. Cum sociis natoque penatibus et magnis dis parturient montes, nascetur ridiculus mus.Lorem ipsum dolor sit amet, consectetuer adipiscing elit. Aenean commodo ligula eget dolor. Aenean massa. Cum sociis natoque penatibus et magnis dis parturient montes, nascetur ridiculus mus.Lorem ipsum dolor sit amet, consectetuer adipiscing elit. Aenean commodo ligula eget dolor. Aenean massa. Cum sociis natoque penatibus et magnis dis parturient montes, nascetur ridiculus mus.Lorem ipsum dolor sit amet, consectetuer adipiscing elit. Aenean commodo ligula eget dolor. Aenean massa. Cum sociis natoque penatibus et magnis dis parturient montes, nascetur ridiculus mus.<span class="more">more ..</span></p>

    <h2 class="abs section-title services-title">SERVICES</h2>
    <div class="abs service" style="left:25px">
      <div class="service-photo"><div style="background:linear-gradient(#f4f4f4,#d9d9d9)" role="img" aria-label="Ambulance"></div></div>
      <div class="service-caption">Lorem ipsum dolo</div>
    </div>
    <div class="abs service" style="left:182px">
      <div class="service-photo"><div style="background:linear-gradient(90deg,#3a2e28,#8fa8c6,#cfdcea)" role="img" aria-label="Traveller looking out of an airport window at a plane"></div></div>
      <div class="service-caption">Lorem ipsum dolo</div>
    </div>
    <div class="abs service" style="left:340px">
      <div class="service-photo"><div style="background:linear-gradient(90deg,#e7e7e7,#d9a24a,#6e8aa8,#e8c53a)" role="img" aria-label="Group of young travellers with backpacks"></div></div>
      <div class="service-caption">Lorem ipsum dolo</div>
    </div>
    <div class="abs service" style="left:498px">
      <div class="service-photo"><div style="background:linear-gradient(90deg,#e9eef0,#7fc4b8,#e9eef0)" role="img" aria-label="Medical team in white coats and scrubs"></div></div>
      <div class="service-caption">Lorem ipsum dolo</div>
    </div>
  </main>

  <aside class="abs sidebar">
    <h3 class="abs news-title">Latest News
      <svg width="34" height="26" viewBox="0 0 34 26" aria-hidden="true"><rect x="2" y="3" width="30" height="21" fill="#f4f4f2" stroke="#a9a9a9"/><rect x="6" y="7" width="12" height="3" fill="#888"/><path d="M6 13 H28 M6 16 H28 M6 19 H28" stroke="#b5b5b5"/></svg>
    </h3>
    <div class="abs news-item" style="top:54px">
      <div class="news-date">Dec 11th</div>
      <div class="news-text">Lorem ipsum dolor sit amet, consectetuer adipiscing elit. Aenean commodo ligula eget dolor. Aenean massa.</div>
    </div>
    <div class="abs news-rule"></div>
    <div class="abs news-item" style="top:138px">
      <div class="news-date">Dec 11th</div>
      <div class="news-text">Lorem ipsum dolor sit amet, consectetuer adipiscing elit. Aenean commodo ligula eget dolor. Aenean massa.</div>
    </div>
    <div class="abs news-more">more ..</div>
  </aside>

  <div class="abs newsletter">
    <h3 class="abs newsletter-title">Newsletter
      <svg width="44" height="26" viewBox="0 0 44 26" aria-hidden="true"><rect x="1" y="1" width="42" height="24" rx="2" fill="#f7c63a" stroke="#d9a21a"/><path d="M1 1 L22 15 L43 1" fill="none" stroke="#d9a21a" stroke-width="1.5"/></svg>
    </h3>
    <div class="abs newsletter-input">Enter your e-mail here:</div>
    <div class="abs newsletter-btn">Subscribe
      <svg width="8" height="10" viewBox="0 0 8 10" aria-hidden="true"><path d="M0 0 L8 5 L0 10 Z" fill="#4a9fd8"/></svg>
    </div>
  </div>

  <footer>
    <div class="abs footer-rule"></div>
    <div class="abs footer-nav">
      <span>Home</span><span class="sep">|</span>
      <span>About Us</span><span class="sep">|</span>
      <span>VIP Club</span><span class="sep">|</span>
      <span>Services</span><span class="sep">|</span>
      <span>Packages and Prices</span><span class="sep">|</span>
      <span>Registration</span><span class="sep">|</span>
      <span>Testimonials</span><span class="sep">|</span>
      <span>Contacts</span>
    </div>
    <div class="abs copyright">© Copyright 2009 - 2010. Your Site Name Dot Com. All Rights Reserved</div>
  </footer>

</div>
</body>
</html>
```